I want a double sided flyer possibly with a picture of a lawn or grass.
Company name, phone number, email, and logo
Halvorsen Turf Management, (404)726-1853,Halvorsen_Turf@brevimail.com
Company services
Fertilization and weed control,Lawn and Landscape maintenance, mowing, pruning, aeration, landscape and Christmas lights,

```html
<!DOCTYPE html>
<html lang="en">
<head>
<meta charset="utf-8">
<title>Halvorsen Turf Management Flyer</title>
<link rel="stylesheet" href="https://fonts.googleapis.com/css2?family=Fira+Sans+Extra+Condensed:wght@400;600&display=swap">
<style>
  :root {
    --backdrop: #5f6169;
    --grass-light: #5aa231;
    --grass-mid: #2f6e1c;
    --grass-dark: #0c2709;
    --cream: #f3ead3;
    --white: #ffffff;
    --divider: rgba(255,255,255,0.85);
  }
  * { margin: 0; padding: 0; box-sizing: border-box; }
  html, body { width: 1200px; height: 1000px; overflow: hidden; }
  body {
    background: var(--backdrop);
    font-family: "Fira Sans Extra Condensed", "Arial Narrow", sans-serif;
    position: relative;
  }
  .flyer {
    position: absolute;
    left: 262px; top: 22px;
    width: 676px; height: 956px;
    overflow: hidden;
  }
  .grass-photo {
    position: absolute; inset: 0;
    background:
      radial-gradient(ellipse 70% 45% at 50% 38%, var(--grass-light) 0%, var(--grass-mid) 55%, transparent 100%),
      linear-gradient(180deg, var(--grass-mid) 0%, #1f4f14 55%, var(--grass-dark) 100%);
  }
  .brand {
    position: absolute; left: 0; right: 0; top: 250px;
    text-align: center; color: var(--cream);
    font-weight: 600;
  }
  .brand-mark {
    width: 150px; height: 150px; border-radius: 50%;
    background: var(--cream);
    margin: 0 auto 80px;
  }
  .brand-name {
    font-size: 96px; line-height: 0.9; letter-spacing: 1px;
    text-transform: uppercase;
  }
  .brand-sub { font-size: 38px; line-height: 1.1; margin-top: 4px; }
  .services {
    position: absolute; left: 20px; right: 20px; top: 676px;
    display: flex; justify-content: center;
    list-style: none; color: var(--white);
    font-weight: 600; font-size: 18px; line-height: 1.05;
    text-transform: uppercase; text-align: center;
  }
  .services li { padding: 0 12px; }
  .services li + li { border-left: 1.5px solid var(--divider); }
  .contact {
    position: absolute; left: 0; right: 0; top: 856px;
    text-align: center; color: var(--white); font-weight: 400;
  }
  .contact-lead { font-size: 19px; }
  .contact-line { font-size: 25px; margin-top: 2px; }
  .contact strong { font-weight: 600; }
</style>
</head>
<body>
  <section class="flyer">
    <div class="grass-photo" role="img" aria-label="Close-up photograph of lush green lawn grass"></div>

    <div class="brand">
      <div class="brand-mark"></div>
      <div class="brand-name">Halvorsen</div>
      <div class="brand-sub">Turf Management</div>
    </div>

    <ul class="services">
      <li>Fertilization<br>&amp; Aeration</li>
      <li>Weed<br>Control</li>
      <li>Lawn/Landscape<br>Maintenance</li>
      <li>Mowing &amp;<br>Pruning</li>
      <li>Landscape<br>Design</li>
      <li>Christmas<br>Lights</li>
    </ul>

    <div class="contact">
      <p class="contact-lead">For a <strong>FREE</strong> quote or more information...</p>
      <p class="contact-line">call <strong>(404) 726-1853</strong> or email <strong>Halvorsen_Turf@brevimail.com</strong></p>
    </div>
  </section>
</body>
</html>
```